looking to have a web site for the company which provides services in the industrial and commercial sectors such as: electrical, automation control and system integration, construction and maintenance, millwright, equipment assembly repair and installation. I have the domain already brivanholdings.net and logo. Most recent projects fulfilled for the following clients: MarlowKibbleCo, Dunholt University, OKSU, FALSTO, Tazzik, Prairie Grains

Target Market(s)

industrial and commercial sectors in electrical, automation, millwright and fabrication fields

Industry/Entity Type

Industrial

Coding

Coded - Design and coding required

Number of Pages Required

5+ page

Font styles to use
Sans Serif

Colors

Designer to choose colors to be used in the design.

Requirements
Nice to have
• looking to get something not complicated, nicely presented with minimum or no scrolling

```html
<!DOCTYPE html>
<html lang="en">
<head>
<meta charset="utf-8">
<title>Brivan Group Ltd — Industrial &amp; Commercial Services</title>
<link rel="stylesheet" href="https://fonts.googleapis.com/css2?family=Montserrat:wght@400;600;700&family=Roboto:ital,wght@0,400;0,500;0,700;1,500&display=swap">
<style>
:root{
  --blue:#0b5e9c;
  --blue-dark:#094d80;
  --ink:#333;
  --text:#555;
  --muted:#999;
  --line:#e2e2e2;
  --card:#f4f4f4;
  --dark:#454545;
  --footer:#3f3f3f;
  --white:#fff;
  --star:#f2b01e;
}
*{box-sizing:border-box;margin:0;padding:0}
html,body{width:1200px;height:3046px;overflow:hidden}
body{font-family:"Roboto",Arial,sans-serif;color:var(--text);background:var(--white);font-size:13px;line-height:1.55}
.wrap{width:876px;margin:0 auto;position:relative}
.btn{display:inline-block;background:var(--blue);color:var(--white);font-size:13px;padding:0;height:38px;line-height:38px;width:114px;text-align:center;border-radius:3px;text-decoration:none}
.section-title{font-family:"Montserrat",Arial,sans-serif;font-weight:700;font-size:31px;line-height:40px;color:var(--ink);text-align:center;text-transform:uppercase;letter-spacing:.3px}
.section-title span{color:var(--blue)}

/* header */
.site-header{height:88px;position:relative}
.brand{position:absolute;left:162px;top:26px;display:flex;align-items:center;gap:10px}
.brand-mark{width:26px;height:26px;background:var(--blue)}
.brand-name{font-family:"Roboto",sans-serif;font-weight:700;font-size:26px;line-height:32px;color:var(--blue);letter-spacing:1px}
.contact-bar{position:absolute;left:578px;top:12px;display:flex;gap:32px;font-size:12px;color:var(--ink);align-items:center}
.contact-bar span{display:flex;align-items:center;gap:8px}
.main-nav{position:absolute;left:460px;top:46px;width:510px;border-top:1px solid var(--line);display:flex;justify-content:space-between;padding:0 12px}
.main-nav a{font-size:12px;color:var(--ink);text-decoration:none;text-transform:uppercase;padding-top:12px;height:42px;position:relative}
.main-nav a.active::before{content:"";position:absolute;left:-12px;right:-12px;top:-2px;height:3px;background:var(--blue)}
.search-btn{position:absolute;left:993px;top:26px;width:38px;height:38px;border-radius:4px;background:var(--blue);display:flex;align-items:center;justify-content:center}

/* hero */
.hero{height:489px;position:relative;background:linear-gradient(90deg,#8e9398 0%,#b7bcc0 28%,#7d8288 48%,#9aa1a6 66%,#c7ccd0 82%,#8a9a78 100%)}
.hero::after{content:"";position:absolute;inset:0;background:rgba(30,35,40,.25)}
.hero-content{position:absolute;left:0;right:0;top:160px;text-align:center;z-index:1;color:var(--white)}
.hero h1{font-family:"Montserrat",sans-serif;font-weight:700;font-size:46px;line-height:56px;letter-spacing:.5px;text-shadow:0 1px 3px rgba(0,0,0,.4)}
.hero p{font-size:18px;text-transform:uppercase;margin-top:2px}
.hero-actions{margin-top:26px;display:flex;justify-content:center;gap:22px}
.hero-actions .btn{width:106px}
.btn-light{background:var(--white);color:var(--blue);border:2px solid var(--blue);line-height:34px}

/* welcome */
.welcome{height:280px;border-bottom:1px solid var(--line);text-align:center;padding-top:50px}
.welcome p{width:700px;margin:12px auto 0;font-size:12.5px;line-height:1.7}
.welcome .btn{margin-top:18px}

/* services */
.services{height:808px;padding-top:44px;text-align:center}
.service-grid{display:flex;flex-wrap:wrap;gap:24px;margin-top:20px;text-align:left}
.service-card{width:276px;height:284px;background:var(--card);border:1px solid var(--line);border-radius:3px;overflow:hidden}
.service-card.wide{width:426px;height:252px}
.service-card.is-active{border-color:#8aa8c4}
.service-photo{height:165px;position:relative}
.service-photo.ph1{background:linear-gradient(135deg,#7a7d80,#b9b2a6 50%,#6e6e6e)}
.service-photo.ph2{background:linear-gradient(135deg,#4f6f84,#9cb4c2 50%,#5d7686)}
.service-photo.ph3{background:linear-gradient(135deg,#8b8478,#cfc8ba 50%,#7e776c)}
.service-photo.ph4{background:linear-gradient(90deg,#6b5f58,#a9a5a0 40%,#5c5652 70%,#8d8783)}
.link-badge{position:absolute;left:50%;top:50%;width:36px;height:36px;margin:-18px 0 0 -18px;border-radius:50%;background:var(--white);display:flex;align-items:center;justify-content:center}
.service-card h3{font-family:"Montserrat",sans-serif;font-weight:600;font-size:14px;color:var(--ink);text-transform:uppercase;margin:14px 20px 4px;line-height:1.3}
.service-card p{font-size:11.5px;line-height:1.6;margin:0 20px}
.service-card.is-active h3{color:var(--blue)}
.services .btn{margin-top:44px}

/* projects */
.projects{height:452px;background:var(--dark);text-align:center;padding-top:50px}
.projects .section-title{color:var(--white)}
.project-tabs{display:inline-flex;margin-top:18px;border:1px solid #bbb;border-radius:2px}
.project-tabs span{width:127px;height:36px;line-height:36px;color:var(--white);font-size:12px;text-transform:uppercase;border-left:1px solid #bbb}
.project-tabs span:first-child{border-left:0;background:var(--blue)}
.project-grid{display:flex;gap:22px;margin-top:30px;text-align:left}
.project-card{width:202px;height:172px;border-radius:4px;overflow:hidden;position:relative;box-shadow:0 3px 8px rgba(0,0,0,.35)}
.pc1{background:linear-gradient(135deg,#8d9197,#d2d4d6 55%,#6f7378)}
.pc2{background:linear-gradient(135deg,#3c7ab0,#9fb8c9 55%,#51627a)}
.pc3{background:linear-gradient(135deg,#5f6265,#a8abad 55%,#4c4f52)}
.pc4{background:linear-gradient(135deg,#3f7db5,#a6bccb 55%,#5b6b80)}
.project-card .view{position:absolute;left:50%;top:48px;transform:translateX(-50%);background:var(--white);color:var(--ink);font-size:11.5px;padding:4px 12px;border-radius:3px;white-space:nowrap}
.project-caption{position:absolute;left:0;right:0;bottom:0;height:48px;background:var(--white);padding:8px 16px;line-height:1.3}
.project-caption b{display:block;font-weight:400;font-size:12px;color:var(--ink);text-transform:uppercase}
.project-caption i{font-size:12px;color:var(--blue);font-weight:500}
.projects .btn{margin-top:28px}

/* testimonials */
.testimonials{height:349px;padding-top:48px;text-align:center}
.testimonial-grid{display:flex;gap:24px;margin-top:30px;text-align:left}
.testimonial{width:426px;height:172px;background:var(--card);border:1px solid var(--line);border-radius:3px;position:relative}
.quote-icon{position:absolute;left:28px;top:-14px;width:38px;height:38px;border-radius:50%;background:var(--white);border:2px solid var(--blue);display:flex;align-items:center;justify-content:center;color:var(--blue);font-family:Georgia,serif;font-size:28px;font-weight:700;line-height:1;padding-top:10px}
.quote-icon.plain{border:0;background:none}
.testimonial p{font-size:11.5px;line-height:1.6;margin:34px 22px 0}
.testimonial-author{position:absolute;left:0;right:0;bottom:0;height:70px;border-top:2px solid #cfdcea;display:flex;align-items:center;padding:0 20px}
.avatar{width:50px;height:50px;border-radius:50%;background:#7fc6b3}
.author-name{margin-left:16px;line-height:1.2}
.author-name b{display:block;font-weight:400;font-size:15px;color:var(--ink)}
.author-name small{font-size:11px;color:var(--muted)}
.stars{margin-left:auto;color:var(--star);font-size:14px;letter-spacing:1px}
.dots{display:flex;justify-content:center;gap:6px;margin-top:16px}
.dots i{width:9px;height:9px;border-radius:50%;border:1px solid #8aa8c4}
.dots i.on{background:var(--blue);border-color:var(--blue)}

/* partners */
.partners{height:250px;text-align:center;padding-top:22px}
.partner-band{margin-top:22px;height:104px;border-top:1px solid var(--line);border-bottom:1px solid var(--line);display:flex;justify-content:center;align-items:center;gap:34px}
.partner-band i{display:block;background:#b4b4b4}
.partner-band i.p2{background:none;border:0 solid #b8b8b8;border-width:6px 0}
.partner-band i.p4{border-radius:50%;background:#c4c4c4}
.partner-band i.p5{background:none;border-bottom:5px solid #bdbdbd}

/* footer */
.site-footer{height:330px;background:var(--footer);color:#e8e8e8;position:relative}
.footer-col{position:absolute;top:54px}
.footer-col h4{font-family:"Montserrat",sans-serif;font-weight:700;font-size:16px;line-height:22px;color:var(--white);text-transform:uppercase;margin-bottom:16px}
.footer-col p{font-size:11.5px;line-height:1.35}
.f-about{left:162px;width:205px}
.f-links{left:423px}
.f-links a{display:block;color:#eee;font-size:12.5px;text-decoration:none;line-height:22px}
.f-news{left:611px;width:190px}
.news-item{display:flex;gap:10px;padding-bottom:10px;margin-bottom:12px;border-bottom:1px solid #5a5a5a}
.news-item:last-child{border:0}
.news-thumb{width:58px;height:58px;flex:none;background:linear-gradient(135deg,#5b7fa0,#c0a98c)}
.news-item p{font-size:11.5px;line-height:1.3}
.news-item small{display:flex;align-items:center;gap:6px;font-size:10.5px;margin-top:6px;color:#ddd}
.f-signup{left:835px;width:203px}
.f-signup input{display:block;width:203px;height:38px;border:0;background:#8c8c8c;color:#eee;padding:0 10px;font:11px "Roboto",sans-serif;margin-top:16px}
.f-signup input::placeholder{color:#f0f0f0}
.f-signup .btn{display:block;width:203px;margin-top:12px;border-radius:0}
.copyright{position:absolute;left:162px;right:162px;bottom:0;height:56px;border-top:1px solid #666;text-align:center;line-height:54px;font-size:11.5px}
</style>
</head>
<body>

<header class="site-header">
  <div class="brand"><span class="brand-mark"></span><span class="brand-name">BRIVAN GROUP LTD</span></div>
  <div class="contact-bar">
    <span><svg width="14" height="11" viewBox="0 0 14 11"><rect x="0.5" y="0.5" width="13" height="10" rx="1" fill="#0b5e9c"/><path d="M1 1l6 5 6-5" stroke="#fff" fill="none"/></svg>info@brivanholdings.net</span>
    <span><svg width="13" height="13" viewBox="0 0 24 24"><path fill="#0b5e9c" d="M6.6 10.8a15 15 0 006.6 6.6l2.2-2.2a1 1 0 011-.25 11.4 11.4 0 003.6.57 1 1 0 011 1V20a1 1 0 01-1 1A17 17 0 013 4a1 1 0 011-1h3.5a1 1 0 011 1 11.4 11.4 0 00.57 3.6 1 1 0 01-.25 1z"/></svg>+00 321 654 0987</span>
  </div>
  <nav class="main-nav">
    <a class="active" href="#">Home</a><a href="#">About</a><a href="#">Services</a><a href="#">Projects</a><a href="#">News</a><a href="#">Contact</a>
  </nav>
  <a class="search-btn" href="#" aria-label="Search"><svg width="16" height="16" viewBox="0 0 16 16"><circle cx="6.5" cy="6.5" r="5" stroke="#fff" stroke-width="2" fill="none"/><path d="M10.5 10.5l4 4" stroke="#fff" stroke-width="2.4" stroke-linecap="round"/></svg></a>
</header>

<section class="hero" role="img" aria-label="Photo of steel grain silos and a loading tower beside a rail line">
  <div class="hero-content">
    <h1>BUILD YOUR DREAM</h1>
    <p>Provides services in the industrial and commercial sectors</p>
    <div class="hero-actions"><a class="btn" href="#">Get Started</a><a class="btn btn-light" href="#">Learn More</a></div>
  </div>
</section>

<section class="welcome">
  <h2 class="section-title">Welcome to <span>Brivan</span></h2>
  <p>Lorem Ipsum is simply dummy text of the printing and typesetting industry. Lorem Ipsum has been the industry's standard dummy text ever since the 1500s, when an unknown printer took a galley of type and scrambled it to make a type specimen book. It has survived not only five centuries, but also the leap into electronic typesetting, remaining essentially unchanged. It was popularised in the 1960s with the release of Letraset sheets containing Lorem Ipsum passages, and more recently.</p>
  <a class="btn" href="#">Read More</a>
</section>

<section class="services">
  <div class="wrap">
    <h2 class="section-title">Our <span>Servies</span></h2>
    <div class="service-grid">
      <article class="service-card">
        <div class="service-photo ph1" role="img" aria-label="Photo of an electrical control panel"></div>
        <h3>Electrical</h3>
        <p>Lorem Ipsum is simply dummy text of the printing and typesetting industry.Lorem Ipsum is simply dummy text.</p>
      </article>
      <article class="service-card is-active">
        <div class="service-photo ph2" role="img" aria-label="Photo of an automated production line">
          <span class="link-badge"><svg width="16" height="16" viewBox="0 0 24 24" fill="none" stroke="#0b5e9c" stroke-width="2.6" stroke-linecap="round"><path d="M10 14a4 4 0 005.7 0l3-3a4 4 0 00-5.7-5.7l-1 1"/><path d="M14 10a4 4 0 00-5.7 0l-3 3a4 4 0 005.7 5.7l1-1"/></svg></span>
        </div>
        <h3>Automation Control</h3>
        <p>Lorem Ipsum is simply dummy text of the printing and typesetting industry.Lorem Ipsum is simply dummy text.</p>
      </article>
      <article class="service-card">
        <div class="service-photo ph3" role="img" aria-label="Photo of steel framework under construction"></div>
        <h3>Construction and Maintenance</h3>
        <p>Lorem Ipsum is simply dummy text of the printing and typesetting industry.Lorem Ipsum is simply dummy text.</p>
      </article>
      <article class="service-card wide">
        <div class="service-photo ph4" role="img" aria-label="Photo of industrial piping and machinery"></div>
        <h3>Millwright</h3>
        <p>Lorem Ipsum is simply dummy text of the printing and typesetting industry.Lorem Ipsum is simply dummy text.</p>
      </article>
      <article class="service-card wide">
        <div class="service-photo ph4" role="img" aria-label="Photo of installed plant equipment"></div>
        <h3>Equipment Assembly Repair and Installation</h3>
        <p>Lorem Ipsum is simply dummy text of the printing and typesetting industry.Lorem Ipsum is simply dummy text.</p>
      </article>
    </div>
    <a class="btn" href="#">View All</a>
  </div>
</section>

<section class="projects">
  <div class="wrap">
    <h2 class="section-title">Our <span>Projects</span></h2>
    <div class="project-tabs"><span>Most Recent</span><span>Electrical</span><span>Automation</span><span>Millwright</span><span>Fabrication</span></div>
    <div class="project-grid">
      <div class="project-card pc1" role="img" aria-label="Photo of an electrical switchboard"></div>
      <div class="project-card pc2" role="img" aria-label="Photo of industrial robot arms">
        <span class="view">View Project</span>
        <div class="project-caption"><b>System Integration</b><i>Automation</i></div>
      </div>
      <div class="project-card pc3" role="img" aria-label="Photo of stainless steel process tanks"></div>
      <div class="project-card pc4" role="img" aria-label="Photo of a robotic welding cell"></div>
    </div>
    <a class="btn" href="#">View All</a>
  </div>
</section>

<section class="testimonials">
  <div class="wrap">
    <h2 class="section-title">Our <span>Testimonials</span></h2>
    <div class="testimonial-grid">
      <article class="testimonial">
        <span class="quote-icon">&ldquo;</span>
        <p>Lorem ipsum dolor sit amet ment bonim sea. Ei explicari evertitur up-tatum vi core zupitor incidenit reforin alienum. Ei explicari evertitur up-tatum vi core zupitor incidenit reforin alienum</p>
        <div class="testimonial-author"><span class="avatar" role="img" aria-label="Client portrait"></span><span class="author-name"><b>Client Name</b><small>City name</small></span><span class="stars">★★★★★</span></div>
      </article>
      <article class="testimonial">
        <span class="quote-icon plain">&ldquo;</span>
        <p>Lorem ipsum dolor sit amet ment bonim sea. Ei explicari evertitur up-tatum vi core zupitor incidenit reforin alienum. Ei explicari evertitur up-tatum vi core zupitor incidenit reforin alienum</p>
        <div class="testimonial-author"><span class="avatar" role="img" aria-label="Client portrait"></span><span class="author-name"><b>Client Name</b><small>City name</small></span><span class="stars">★★★★★</span></div>
      </article>
    </div>
    <div class="dots"><i></i><i class="on"></i><i></i></div>
  </div>
</section>

<section class="partners">
  <h2 class="section-title">Our <span>Partner</span></h2>
  <div class="partner-band">
    <i class="p1" style="width:148px;height:40px" role="img" aria-label="MarlowKibbleCo badge"></i>
    <i class="p2" style="width:156px;height:30px" role="img" aria-label="Tazzik badge"></i>
    <i class="p3" style="width:120px;height:50px" role="img" aria-label="Dunholt University badge"></i>
    <i class="p4" style="width:126px;height:66px" role="img" aria-label="OKSU badge"></i>
    <i class="p5" style="width:130px;height:48px" role="img" aria-label="Prairie Grains badge"></i>
  </div>
</section>

<footer class="site-footer">
  <div class="footer-col f-about">
    <h4>About Us</h4>
    <p>Lorem Ipsum is simply dummy text of the printing and typesetting industry. Lorem Ipsum has been the industry's standard dummy text ever since the 1500s, when an unknown printer took a galley of type and scrambled it to make a type specimen book.</p>
  </div>
  <div class="footer-col f-links">
    <h4>Quicklinks</h4>
    <a href="#">Home</a><a href="#">About</a><a href="#">Services</a><a href="#">Projects</a><a href="#">News</a><a href="#">Contact</a>
  </div>
  <div class="footer-col f-news">
    <h4>Latest News</h4>
    <div class="news-item"><span class="news-thumb" role="img" aria-label="News photo of a technician at work"></span><div><p>Proffesional solutions for your business.</p><small><svg width="10" height="10" viewBox="0 0 10 10"><rect x="0.5" y="1.5" width="9" height="8" fill="none" stroke="#ddd"/><path d="M0.5 4h9" stroke="#ddd"/></svg>Jan 30, 2017</small></div></div>
    <div class="news-item"><span class="news-thumb" role="img" aria-label="News photo of a technician at work"></span><div><p>Proffesional solutions for your business.</p><small><svg width="10" height="10" viewBox="0 0 10 10"><rect x="0.5" y="1.5" width="9" height="8" fill="none" stroke="#ddd"/><path d="M0.5 4h9" stroke="#ddd"/></svg>Jan 30, 2017</small></div></div>
  </div>
  <div class="footer-col f-signup">
    <h4>Newsletter</h4>
    <p>Signup for our mailing list to get latest updates and news.</p>
    <input type="email" placeholder="Enter your Email Address">
    <a class="btn" href="#">Subscribe</a>
  </div>
  <div class="copyright">Copyright © 2017 ALL RIGHTS RESERVED</div>
</footer>

</body>
</html>
```